**Designs Wanted for High Profile Banner Ad Campaign**

Our leading Public Relations agency services some of the world's leading brands in our local market.

We now need a banner ad design to support our own growth.

We are looking to have banner ads designed that will carry a common theme to be used across the following sizes (all these sizes will need to be created):
• Vertical rectangle: 240 x 400
• Mobile leaderboard: 320 x 50
• Banner: 468 x 60
• Leaderboard: 728 x 90
• Square: 250 x 250
• Small square: 200 x 200
• Large rectangle: 336 x 280
• Inline rectangle: 300 x 250
• Skyscraper: 120 x 600
• Wide skyscraper: 160 x 600
• Half-page: 300 x 600
• Large leaderboard: 970x90
• Large mobile banner: 320 x 100
• Billboard: 970 x 250

Our primary retargeting and regular display campaign objective is to encourage marketing managers and business owners to visit our site and contact us.
See www.lumenvoicecomms.co.nz for our current look and feel. Please keep consistent colours with that site. Our two logos are attached.

This is our first digital retargeting campaign and we are open to your advice and suggestions on what will encourage click through from potential clients.

Our current thinking at the moment is that the ad could be built around these concepts:
“Reach, socialise, inspire.”
In others words – as a PR agency we help clients ‘reach’ their target market through creating content for news media.
The ‘socialise’ represents engagement through social media – in that we help develop and build their social media presence.
‘Inspire’ refers to the fact we aim to inspire their target market towards engaging with our clients.
Plus a suitable call to action– eg. Click here to meet your public relations needs today.

In terms of designs we are open to suggestion: eg. the adverts could use icons or something else that you have seen work.

We would like to see some eye catching animation, interaction or movement in the advert to.

We need the ad to be effective, eye catching, professional, modern, sophisticated (in that our target market is professional executives) and crisp, clean and uncluttered.

Time is short for us, so please send through designs as soon as possible – don’t wait until the last day!

Additional note: the existing fish image and 'stand out from the crowd' slogan on our home page are not required as part of this design. We have been looking to move towards the new slogan (“Reach, socialise, inspire.” ) and this banner ad may also serve to give us some new direction ideas as well. we do need to keep the existing logo and orange colour though.

Target Market(s)

Business to Business. Marketing and brand managers, Small, Medium and large business owners and executives.
Those with a business in the New Zealand market.

Industry/Entity Type

Marketing

Requirements
Must have
• our logo
animation or movement
orange colour/ consistency with our existing website.
our proposed slogan: “Reach, socialise, inspire.” (however we are open to seeing alternative ideas as well if you want to submit more than one concept)
call to action.
Should not have
• read note about existing fish and slogan above.

```html
<!DOCTYPE html>
<html lang="en">
<head>
<meta charset="utf-8">
<title>Lumenvoice – Public Relation Banner Set</title>
<link rel="stylesheet" href="https://fonts.googleapis.com/css2?family=Arimo:wght@400;700&display=swap">
<style>
:root{
  --orange:#ff6a00;
  --orange-light:#ff9a2e;
  --yellow:#f6dc12;
  --dark:#2d2c2e;
  --band:#5b5a5d;
  --blue:#1d9ad6;
  --grey-text:#4a4a4a;
  --white:#ffffff;
  --canvas:#ffffff;
}
*{box-sizing:border-box;margin:0;padding:0}
html,body{width:1200px;height:1200px;overflow:hidden;background:var(--canvas)}
body{position:relative;font-family:"Arimo",Arial,sans-serif;font-weight:700}
.banner{position:absolute;overflow:hidden;background:var(--dark);border:1px solid #9a9a9a}
.abs{position:absolute}
.header{position:absolute;left:0;top:0;width:100%;background:var(--white)}
.swoosh{position:absolute;left:0;width:100%;display:block}
.dark-panel{position:absolute;background:var(--dark);color:var(--white);text-align:center;line-height:1.12;text-shadow:0 1px 2px rgba(0,0,0,.6)}
.dark-panel .hl{color:var(--yellow)}
.photo{position:absolute;background:linear-gradient(160deg,#eef0f2 0%,#c9ccd2 35%,#e7d9c6 65%,#f3ece2 100%)}
.band{position:absolute;left:0;width:100%;background:var(--band);color:var(--white);text-align:center;line-height:1.15}
.cta{position:absolute;display:flex;align-items:center;justify-content:center;gap:10px;border-radius:4px;
  background:linear-gradient(180deg,var(--orange-light) 0%,var(--orange) 60%,#e65a00 100%);
  color:#5a2a00;box-shadow:0 2px 4px rgba(0,0,0,.5)}
.cta .arrow{display:block;border-radius:50%;background:#4a2208}
.base{position:absolute;left:0;bottom:0;width:100%;height:8px;background:linear-gradient(90deg,#777,#eee,#888)}
.brand{position:absolute;color:#7a7a7a;font-weight:400;letter-spacing:2px}
.title-grey{color:var(--grey-text)}
.title-orange{color:var(--orange)}
</style>
</head>
<body>

<!-- Leaderboard -->
<section class="banner leaderboard" style="left:17px;top:17px;width:1026px;height:127px">
  <div class="header" style="width:270px;height:127px;text-align:center;padding-top:24px;line-height:1.1">
    <div class="title-grey" style="font-size:22px">PUBLIC RELATION</div>
    <div class="title-orange" style="font-size:25px">FOR SMALL<br>BUSINESS</div>
  </div>
  <svg class="abs" style="left:250px;top:0" width="40" height="127" viewBox="0 0 40 127" preserveAspectRatio="none">
    <path d="M0,0 H14 Q36,63 14,127 H0 Z" fill="var(--white)"/>
    <path d="M14,0 H24 Q44,63 24,127 H14 Q36,63 14,127 Z" fill="var(--blue)"/>
  </svg>
  <div class="dark-panel" style="left:278px;top:0;width:192px;height:127px;padding-top:8px;font-size:23px">We are PR<br>Specialist <span class="hl">&amp;</span><br><span class="hl">as Marketing<br>Consultants</span></div>
  <div class="photo" role="img" aria-label="Photo of two business colleagues reviewing a tablet" style="left:470px;top:0;width:310px;height:127px"></div>
  <svg class="abs" style="left:760px;top:0" width="40" height="127" viewBox="0 0 40 127" preserveAspectRatio="none">
    <path d="M40,0 H22 Q0,63 22,127 H40 Z" fill="var(--orange)"/>
    <path d="M40,0 H30 Q10,63 30,127 H40 Z" fill="var(--dark)"/>
  </svg>
  <div class="band" style="left:790px;top:0;width:236px;height:60px;padding-top:7px;font-size:18px">has experience 20 years<br>in New Zealand</div>
  <div class="cta" style="left:820px;top:70px;width:168px;height:48px;font-size:20px">Join Now
    <svg class="arrow" width="32" height="32" viewBox="0 0 32 32"><path d="M13,9 L20,16 L13,23" stroke="#fff" stroke-width="3.5" fill="none"/></svg></div>
</section>

<!-- Large rectangle -->
<section class="banner square-large" style="left:18px;top:172px;width:424px;height:350px">
  <div class="header" style="height:70px">
    <div class="brand" style="left:10px;top:10px;font-size:20px">LUMENVOICE</div>
    <div class="abs title-grey" style="left:176px;top:4px;font-size:21px">PUBLIC RELATION</div>
    <div class="abs title-orange" style="left:170px;top:26px;font-size:18px">FOR SMALL BUSINESS</div>
  </div>
  <svg class="swoosh" style="top:44px" width="424" height="30" viewBox="0 0 424 30" preserveAspectRatio="none">
    <path d="M0,6 Q212,30 424,6 V30 H0 Z" fill="var(--dark)"/>
    <path d="M0,0 Q212,22 424,0 V8 Q212,32 0,8 Z" fill="var(--blue)"/>
  </svg>
  <div class="dark-panel" style="left:0;top:80px;width:170px;height:150px;padding-top:10px;font-size:23px;line-height:1.3">We are PR<br>Specialist <span class="hl">&amp;</span><br><span class="hl">as Marketing<br>Consultants</span></div>
  <div class="photo" role="img" aria-label="Photo of two business colleagues reviewing a tablet" style="left:170px;top:68px;width:254px;height:180px"></div>
  <svg class="swoosh" style="top:226px" width="424" height="26" viewBox="0 0 424 26" preserveAspectRatio="none">
    <path d="M0,22 Q212,-6 424,22 V26 H0 Z" fill="var(--orange)"/>
  </svg>
  <div class="band" style="top:246px;height:40px;padding-top:10px;font-size:18px">has experience 20 years in New Zealand</div>
  <div class="cta" style="left:127px;top:297px;width:166px;height:46px;font-size:20px">Click Here
    <svg class="arrow" width="32" height="32" viewBox="0 0 32 32"><path d="M13,9 L20,16 L13,23" stroke="#fff" stroke-width="3.5" fill="none"/></svg></div>
</section>

<!-- Square -->
<section class="banner square" style="left:18px;top:535px;width:353px;height:350px">
  <div class="header" style="height:66px">
    <div class="brand" style="left:8px;top:12px;font-size:17px;letter-spacing:1px">LUMENVOICE</div>
    <div class="abs title-grey" style="left:158px;top:6px;font-size:18px">PUBLIC RELATION</div>
    <div class="abs title-orange" style="left:154px;top:27px;font-size:15px">FOR SMALL BUSINESS</div>
  </div>
  <svg class="swoosh" style="top:44px" width="353" height="30" viewBox="0 0 353 30" preserveAspectRatio="none">
    <path d="M0,6 Q176,30 353,6 V30 H0 Z" fill="var(--dark)"/>
    <path d="M0,0 Q176,22 353,0 V8 Q176,32 0,8 Z" fill="var(--blue)"/>
  </svg>
  <div class="dark-panel" style="left:0;top:100px;width:170px;height:130px;font-size:21px;line-height:1.23">We are PR<br>Specialist <span class="hl">&amp;</span><br><span class="hl">as Marketing<br>Consultants</span></div>
  <div class="photo" role="img" aria-label="Photo of two business colleagues reviewing a tablet" style="left:168px;top:70px;width:185px;height:180px"></div>
  <svg class="swoosh" style="top:224px" width="353" height="28" viewBox="0 0 353 28" preserveAspectRatio="none">
    <path d="M0,24 Q176,-6 353,24 V28 H0 Z" fill="var(--orange)"/>
  </svg>
  <div class="band" style="top:248px;height:36px;padding-top:9px;font-size:15.5px">has experience 20 years in New Zealand</div>
  <div class="cta" style="left:101px;top:293px;width:150px;height:42px;font-size:17px">Click Here
    <svg class="arrow" width="28" height="28" viewBox="0 0 32 32"><path d="M13,9 L20,16 L13,23" stroke="#fff" stroke-width="3.5" fill="none"/></svg></div>
  <div class="base" style="height:6px"></div>
</section>

<!-- Half-page -->
<section class="banner half-page" style="left:487px;top:172px;width:424px;height:844px">
  <div class="header" style="height:130px;text-align:center;padding-top:10px;line-height:1.03">
    <div class="title-grey" style="font-size:31px">PUBLIC RELATION</div>
    <div class="title-orange" style="font-size:38px">FOR SMALL<br>BUSINESS</div>
  </div>
  <svg class="swoosh" style="top:114px" width="424" height="44" viewBox="0 0 424 44" preserveAspectRatio="none">
    <path d="M0,10 Q212,44 424,10 V44 H0 Z" fill="var(--dark)"/>
    <path d="M0,0 Q212,30 424,0 V12 Q212,44 0,12 Z" fill="var(--blue)"/>
  </svg>
  <div class="dark-panel" style="left:0;top:172px;width:424px;height:130px;font-size:31px;line-height:1.12">We are PR Specialist<br><span class="hl">&amp; as Marketing<br>Consultants</span></div>
  <div class="photo" role="img" aria-label="Photo of two business colleagues reviewing a tablet" style="left:0;top:304px;width:424px;height:340px"></div>
  <div class="brand" style="left:134px;top:312px;font-size:27px;letter-spacing:2px">LUMENVOICE</div>
  <svg class="swoosh" style="top:612px" width="424" height="36" viewBox="0 0 424 36" preserveAspectRatio="none">
    <path d="M0,32 Q212,-8 424,32 V36 H0 Z" fill="var(--orange)"/>
  </svg>
  <div class="band" style="top:642px;height:104px;padding-top:5px;font-size:29px;line-height:1.1">has experience<br>20 years in New<br>Zealand</div>
  <div class="cta" style="left:76px;top:760px;width:267px;height:62px;font-size:32px;color:#6a3000">Click Here
    <svg class="arrow" width="44" height="44" viewBox="0 0 32 32"><path d="M13,9 L20,16 L13,23" stroke="#fff" stroke-width="3.5" fill="none"/></svg></div>
  <div class="base"></div>
</section>

<!-- Wide skyscraper -->
<section class="banner skyscraper" style="left:957px;top:172px;width:226px;height:844px">
  <div class="header" style="height:150px;text-align:center;padding-top:4px;line-height:1.05">
    <div class="title-grey" style="font-size:25px">PUBLIC<br>RELATION</div>
    <div class="title-orange" style="font-size:32px">FOR SMALL<br>BUSINESS</div>
  </div>
  <svg class="swoosh" style="top:136px" width="226" height="32" viewBox="0 0 226 32" preserveAspectRatio="none">
    <path d="M0,8 Q113,32 226,8 V32 H0 Z" fill="var(--dark)"/>
    <path d="M0,0 Q113,22 226,0 V10 Q113,32 0,10 Z" fill="var(--blue)"/>
  </svg>
  <div class="dark-panel" style="left:0;top:164px;width:226px;height:132px;font-size:27px;line-height:1.12">We are PR<br>Specialist <span class="hl">&amp;</span><br><span class="hl">as Marketing<br>Consultants</span></div>
  <div class="photo" role="img" aria-label="Photo of two business colleagues reviewing a tablet" style="left:0;top:296px;width:226px;height:366px"></div>
  <div class="brand" style="left:22px;top:302px;font-size:24px;letter-spacing:1px">LUMENVOICE</div>
  <svg class="swoosh" style="top:632px" width="226" height="34" viewBox="0 0 226 34" preserveAspectRatio="none">
    <path d="M0,30 Q113,-6 226,30 V34 H0 Z" fill="var(--orange)"/>
  </svg>
  <div class="band" style="top:660px;height:92px;padding-top:7px;font-size:23px;line-height:1.1">has experience<br>20 years in New<br>Zealand</div>
  <div class="cta" style="left:17px;top:763px;width:190px;height:58px;font-size:23px;color:#6a3000">Click Here
    <svg class="arrow" width="38" height="38" viewBox="0 0 32 32"><path d="M13,9 L20,16 L13,23" stroke="#fff" stroke-width="3.5" fill="none"/></svg></div>
  <div class="base"></div>
</section>

</body>
</html>
```